Conservative, Modern and Sharp Builder Business card

Hi there,
We would like to update our existing business card.
I have attached photos of existing business card, logo and van sign.

I would like the business card to also list what we do :
Renovation • New Build • Alteration
Extension • Bathroom • Maintenance.(Seperated by dots)

Contact number : 021 0483 0752
(With that exact spacing)

Ideally when people looking from about 2-3 metres, they know that it is a builder’s business card

Open to suggestions on fonts, layout, style of business card

PLEASE ONLY SUBMIT YOUR BEST OR MAX 3 DESIGNS FOR EACH DESIGNER

Thanks

Industry/Entity Type

Construction. Renovation

Contact Information for Business Card

Details should be the same as the existing card. And addition of what we do.

Requirements
Should not have
• The new business card must not have the same layout as our existing one. Thanks

```html
<!DOCTYPE html>
<html lang="en">
<head>
<meta charset="utf-8">
<title>KeelBuild Business Card</title>
<link href="https://fonts.googleapis.com/css2?family=Saira+Semi+Condensed:wght@600;700&family=Noto+Sans:wght@700&display=swap" rel="stylesheet">
<style>
  :root {
    --backdrop: #aeafb2;
    --card: #edf0f0;
    --ink: #111111;
    --green: #1bbf2e;
    --faint: #dfe2e3;
  }
  * { margin: 0; padding: 0; box-sizing: border-box; }
  html, body { width: 1200px; height: 1200px; overflow: hidden; }
  body {
    background: var(--backdrop);
    position: relative;
    font-family: "Saira Semi Condensed", "Arial Narrow", sans-serif;
    color: var(--ink);
  }
  .card {
    position: absolute;
    left: 212px;
    width: 777px;
    height: 432px;
    background: var(--card);
  }
  .card--front { top: 112px; }
  .card--back { top: 656px; }

  .abs { position: absolute; white-space: nowrap; }

  .person-name {
    left: 0; width: 400px; top: 44px;
    text-align: center;
    font-weight: 700; font-size: 44px; line-height: 50px;
  }
  .name-rule {
    position: absolute; left: 58px; top: 100px; width: 284px; height: 1.5px;
    background: var(--ink);
  }
  .person-role {
    left: 0; width: 400px; top: 106px;
    text-align: center;
    color: var(--green); font-weight: 700; font-size: 30px; line-height: 34px;
  }
  .brand-watermark {
    left: 60px; width: 260px; top: 178px;
    text-align: center;
    font-family: "Noto Sans", sans-serif; font-weight: 700;
    font-size: 52px; color: var(--faint); letter-spacing: -1px;
  }
  .services-title {
    left: 35px; top: 304px;
    color: var(--green); font-weight: 700; font-size: 27px; line-height: 32px;
  }
  .services {
    left: 35px; top: 338px;
    font-weight: 700; font-size: 20px; line-height: 21px;
  }

  .brand-square {
    position: absolute; background: var(--ink);
  }
  .card--front .brand-square { left: 582px; top: 34px; width: 44px; height: 44px; }
  .brand-name {
    font-family: "Noto Sans", sans-serif; font-weight: 700; color: var(--ink);
    letter-spacing: -0.5px;
  }
  .card--front .brand-name {
    left: 454px; width: 300px; top: 105px; text-align: center;
    font-size: 40px; line-height: 50px;
  }

  .contact-list { position: absolute; right: 91px; top: 0; }
  .contact-row {
    position: absolute; right: 0;
    display: flex; align-items: center; gap: 12px;
    font-weight: 700; white-space: nowrap;
  }
  .contact-row svg { width: 34px; height: 34px; flex: none; }
  .contact-row--social { top: 199px; font-size: 27px; }
  .contact-row--phone { top: 247px; font-size: 27px; }
  .contact-row--email { top: 302px; font-size: 20px; }
  .contact-row--web { top: 351px; font-size: 27px; }

  .card--back .brand-square { left: 343px; top: 140px; width: 92px; height: 92px; }
  .card--back .brand-name {
    left: 0; width: 777px; top: 262px; text-align: center;
    font-size: 74px; line-height: 90px;
  }
</style>
</head>
<body>

<section class="card card--front">
  <h1 class="abs person-name">Tomas Kerehoma</h1>
  <div class="name-rule"></div>
  <p class="abs person-role">Residential Builder</p>
  <div class="abs brand-watermark" aria-hidden="true">KeelBuild</div>

  <h2 class="abs services-title">What We Do :</h2>
  <p class="abs services">Renovation • New Build • Alteration<br>Extension • Bathroom • Maintenance</p>

  <div class="brand-square"></div>
  <div class="abs brand-name">KeelBuild</div>

  <div class="contact-list">
    <div class="contact-row contact-row--social">
      <span>KeelBuild.nz</span>
      <svg viewBox="0 0 34 34"><rect x="3" y="3" width="28" height="28" rx="7" fill="none" stroke="var(--green)" stroke-width="3"/></svg>
    </div>
    <div class="contact-row contact-row--phone">
      <span>021 0483 0752</span>
      <svg viewBox="0 0 24 24"><path fill="var(--green)" d="M6.6 10.8c1.4 2.8 3.8 5.1 6.6 6.6l2.2-2.2c.3-.3.7-.4 1-.2 1.1.4 2.3.6 3.6.6.6 0 1 .4 1 1V20c0 .6-.4 1-1 1C10.6 21 3 13.4 3 4c0-.6.4-1 1-1h3.5c.6 0 1 .4 1 1 0 1.3.2 2.5.6 3.6.1.3 0 .7-.2 1l-2.3 2.2z"/></svg>
    </div>
    <div class="contact-row contact-row--email">
      <span>keelbuild@mailbox.co.nz</span>
      <svg viewBox="0 0 34 34"><rect x="1" y="6" width="32" height="22" fill="var(--green)"/><path d="M1 6 L17 19 L33 6 M1 28 L13 16 M33 28 L21 16" fill="none" stroke="var(--card)" stroke-width="2"/></svg>
    </div>
    <div class="contact-row contact-row--web">
      <span>www.KeelBuild.nz</span>
      <svg viewBox="0 0 34 34" fill="none" stroke="var(--green)" stroke-width="2.2"><circle cx="17" cy="17" r="14"/><ellipse cx="17" cy="17" rx="6.5" ry="14"/><path d="M3 17h28M5 10h24M5 24h24M17 3v28"/></svg>
    </div>
  </div>
</section>

<section class="card card--back">
  <div class="brand-square"></div>
  <div class="abs brand-name">KeelBuild</div>
</section>

</body>
</html>
```